Australian Recruitment Agency Flyer

We are looking for a 1 page flyer to promote our recruitment company. We would like this to have a corporate look.

Attached is a word document with the content we would like included in the flyer.

I have also attached some of our clients logos to be included in the flyer

Target Market(s)

Professional organisations looking to hire new staff

Industry/Entity Type

It Company

Colors
85abd2
3176b5
31b7a3
d2a4cc
e667a6
b768aa
876aae
3276b5
f04a50

Requirements
Must have
• Must have the content that we have include on a word document in the design brief.

```html
<!DOCTYPE html>
<html lang="en">
<head>
<meta charset="utf-8">
<title>Talentrise – Recruitment Flyer</title>
<link rel="stylesheet" href="https://fonts.googleapis.com/css2?family=Oswald:wght@500;700&family=Open+Sans:wght@400;600&display=swap">
<style>
  :root {
    --coral: #f04a50;
    --ink: #000000;
    --paper: #ffffff;
    --slate: #3a3f4a;
    --purple: #876aae;
    --grey: #55595f;
  }
  html, body {
    margin: 0;
    padding: 0;
    overflow: hidden;
    background: var(--paper);
  }
  .flyer {
    position: relative;
    width: 1000px;
    height: 1200px;
    overflow: hidden;
    background: var(--paper);
    font-family: "Open Sans", Arial, sans-serif;
  }
  .hero-panel {
    position: absolute;
    left: 83px;
    top: 37px;
    width: 832px;
    height: 791px;
    background: var(--coral);
  }
  .person-photo {
    position: absolute;
    background: linear-gradient(160deg, rgba(90,92,100,0.85) 0%, rgba(55,57,64,0.9) 55%, rgba(40,42,48,0.95) 100%);
  }
  .person-photo.woman {
    left: 232px;
    top: 95px;
    width: 310px;
    height: 733px;
    border-radius: 150px 150px 0 0;
  }
  .person-photo.man {
    left: 450px;
    top: 165px;
    width: 450px;
    height: 663px;
    border-radius: 200px 200px 0 0;
  }
  .section-label {
    position: absolute;
    left: 137px;
    top: 143px;
    font-family: "Oswald", "Arial Narrow", sans-serif;
    font-weight: 700;
    font-size: 27px;
    line-height: 29px;
    letter-spacing: 1.5px;
  }
  .section-label .dark { color: var(--ink); display: block; }
  .section-label .light { color: var(--paper); display: block; }
  .brand {
    position: absolute;
    left: 583px;
    top: 64px;
    display: flex;
    align-items: center;
    gap: 18px;
  }
  .brand-mark {
    width: 70px;
    height: 70px;
    background: var(--purple);
  }
  .brand-name {
    font-family: "Open Sans", Arial, sans-serif;
    font-weight: 600;
    font-size: 40px;
    line-height: 42px;
    color: var(--slate);
  }
  .brand-tagline {
    font-size: 12px;
    color: var(--slate);
    margin-top: 2px;
    padding-left: 6px;
  }
  .headline-block {
    position: absolute;
    left: 0;
    top: 0;
  }
  .headline {
    position: absolute;
    left: 180px;
    font-family: "Oswald", "Arial Narrow", sans-serif;
    font-weight: 700;
    line-height: 1;
    margin: 0;
    white-space: nowrap;
  }
  .headline.we { top: 518px; font-size: 131px; color: var(--paper); letter-spacing: 46px; }
  .headline.help { top: 650px; font-size: 166px; color: var(--coral); letter-spacing: 32px; }
  .headline.you { top: 811px; font-size: 188px; color: var(--paper); letter-spacing: 8px; }
  .intro {
    position: absolute;
    left: 540px;
    top: 840px;
    width: 368px;
    margin: 0;
    font-size: 18px;
    line-height: 24.5px;
    color: var(--ink);
  }
  .intro .accent { color: var(--coral); }
  .slogan-bar {
    position: absolute;
    left: 150px;
    top: 1015px;
    width: 695px;
    height: 73px;
    background: var(--ink);
    display: flex;
    align-items: center;
    justify-content: center;
    font-family: "Oswald", "Arial Narrow", sans-serif;
    font-weight: 700;
    font-size: 56px;
    letter-spacing: 4px;
    color: var(--paper);
  }
  .slogan-bar .accent { color: var(--coral); margin-left: 18px; }
  .client-list {
    position: absolute;
    left: 155px;
    top: 1112px;
    width: 700px;
    height: 48px;
    display: flex;
    align-items: center;
    justify-content: space-between;
    margin: 0;
    padding: 0;
    list-style: none;
  }
  .client {
    font-family: "Open Sans", Arial, sans-serif;
    font-weight: 600;
    font-size: 14px;
    color: var(--grey);
    white-space: nowrap;
  }
</style>
</head>
<body>
<main class="flyer">
  <div class="hero-panel"></div>
  <div class="person-photo woman" role="img" aria-label="Smiling businesswoman in a grey suit with arms crossed"></div>
  <div class="person-photo man" role="img" aria-label="Smiling businessman in a grey suit and red tie offering a handshake"></div>

  <div class="section-label">
    <span class="dark">RECRUITMENT</span>
    <span class="light">RESOURCES</span>
  </div>

  <div class="brand">
    <div class="brand-mark"></div>
    <div>
      <div class="brand-name">Talentrise</div>
      <div class="brand-tagline">Human Resources &amp; Recruitment</div>
    </div>
  </div>

  <svg class="headline-block" width="1000" height="1200" viewBox="0 0 1000 1200" aria-hidden="true">
    <polygon points="150,492 400,492 400,642 640,642 640,828 527,828 527,990 150,990" fill="#000"/>
  </svg>
  <h1 class="headline we">WE</h1>
  <div class="headline help">HELP</div>
  <div class="headline you">YOU</div>

  <p class="intro">Life is filled with <span class="accent">opportunities</span>. We are committed to offering new opportunities to organisations and <span class="accent">people</span> from all walks of life to help them be <span class="accent">successful</span> and to open up new perspectives in life.</p>

  <div class="slogan-bar">OPPORTUNITIES<span class="accent">FOR LIFE</span></div>

  <ul class="client-list">
    <li class="client">Brindlewood Fleet</li>
    <li class="client">Tallowin</li>
    <li class="client">Cobalt Ridge</li>
    <li class="client">Southcross Ore</li>
    <li class="client">Penvale Advisory</li>
    <li class="client">Harwick Process</li>
    <li class="client">Zelto</li>
  </ul>
</main>
</body>
</html>
```